Business Card design for new private practice opening

I need a business card design for my new private practice with my new logo uploaded as a file
On the front the logo
On the back: maybe a small logo somewhere?
Priv. Doz. DDr. Corinna Vestaluk
Fachärztin für Allgemein- & Viszeralchirurgie
Address: xxx
Tel: xxx
Mobil:xxx
Webseite:xxx
Email:xxx

Contact Information for Business Card

See project description above for details

Requirements
Nice to have
• I would like the colors of the logo incorporated into the business card

```html
<!DOCTYPE html>
<html lang="de">
<head>
<meta charset="utf-8">
<title>Vestaluk Chirurgie – Visitenkarte</title>
<link rel="stylesheet" href="https://fonts.googleapis.com/css2?family=Montserrat:wght@300;400;500;600&display=swap">
<style>
  :root {
    --backdrop: #8c8c8c;
    --teal: #45b9b6;
    --white: #ffffff;
  }
  * { margin: 0; padding: 0; box-sizing: border-box; }
  html, body {
    width: 1200px; height: 1200px; overflow: hidden;
    background: var(--backdrop);
    font-family: "Montserrat", Arial, sans-serif;
    color: var(--white);
  }
  .canvas { position: relative; width: 1200px; height: 1200px; }
  .card {
    position: absolute; left: 205px;
    width: 778px; height: 444px;
    background: var(--teal);
    border-radius: 24px;
  }
  .card--front { top: 88px; }
  .card--back { top: 596px; }

  .brand { position: absolute; display: flex; align-items: center; }
  .brand__circle { border: solid var(--white); border-radius: 50%; flex: none; }
  .brand__name { font-weight: 600; letter-spacing: 0.01em; white-space: nowrap; }

  .card--front .brand { left: 93px; top: 135px; }
  .card--front .brand__circle { width: 172px; height: 172px; border-width: 7px; }
  .card--front .brand__name { font-size: 62px; line-height: 72px; margin-left: 28px; }

  .card--back .brand { left: 49px; top: 186px; }
  .card--back .brand__circle { width: 82px; height: 82px; border-width: 4px; }
  .card--back .brand__name { font-size: 29px; line-height: 31px; margin-left: 12px; }

  .divider {
    position: absolute; left: 357px; top: 88px;
    width: 1px; height: 288px; background: var(--white);
  }
  .person { position: absolute; left: 385px; top: 103px; }
  .person__name { font-size: 17px; font-weight: 600; letter-spacing: 0.07em; }
  .person__title { font-size: 12px; font-weight: 300; margin-top: 2px; letter-spacing: 0.03em; }

  .contacts { position: absolute; left: 385px; top: 164px; list-style: none; width: 380px; }
  .contacts__item {
    display: flex; align-items: flex-start;
    font-size: 19px; font-weight: 400; letter-spacing: 0.05em;
    line-height: 22px; margin-bottom: 16px;
  }
  .contacts__icon { width: 24px; height: 24px; flex: none; margin-right: 14px; }
</style>
</head>
<body>
<main class="canvas">
  <section class="card card--front" aria-label="Vorderseite">
    <div class="brand">
      <span class="brand__circle"></span>
      <span class="brand__name">VESTALUK<br>CHIRURGIE</span>
    </div>
  </section>

  <section class="card card--back" aria-label="Rückseite">
    <div class="brand">
      <span class="brand__circle"></span>
      <span class="brand__name">VESTALUK<br>CHIRURGIE</span>
    </div>
    <div class="divider"></div>
    <div class="person">
      <p class="person__name">Priv. Doz. DDr. Corinna Vestaluk</p>
      <p class="person__title">Fachärztin für Allgemein- &amp; Viszeralchirurgie</p>
    </div>
    <ul class="contacts">
      <li class="contacts__item">
        <svg class="contacts__icon" viewBox="0 0 24 24"><circle cx="12" cy="12" r="12" fill="#fff"/><rect x="6" y="8" width="12" height="8" fill="none" stroke="#45b9b6" stroke-width="1.6"/><path d="M6 8l6 5 6-5" fill="none" stroke="#45b9b6" stroke-width="1.6"/></svg>
        <span>xxxxxxxxxxx@vestaluk.de</span>
      </li>
      <li class="contacts__item">
        <svg class="contacts__icon" viewBox="0 0 24 24"><circle cx="12" cy="12" r="12" fill="#fff"/><path d="M8.5 6.5l2 2.5-1.2 1.4a8 8 0 0 0 4.3 4.3l1.4-1.2 2.5 2-1.3 1.8c-4.5-.3-8.6-4.4-9-9z" fill="#45b9b6"/></svg>
        <span>+49 000 000 0000</span>
      </li>
      <li class="contacts__item">
        <svg class="contacts__icon" viewBox="0 0 24 24"><circle cx="12" cy="12" r="12" fill="#fff"/><path d="M5.5 10c0-2.5 13-2.5 13 0v1.2h-3V9.8h-7v1.4h-3z" fill="#45b9b6"/><path d="M8 12h8l1 5H7z" fill="#45b9b6"/><circle cx="12" cy="14.5" r="1.3" fill="#fff"/></svg>
        <span>+49 000 000 0000</span>
      </li>
      <li class="contacts__item">
        <svg class="contacts__icon" viewBox="0 0 24 24"><circle cx="12" cy="12" r="12" fill="#fff"/><g fill="none" stroke="#45b9b6" stroke-width="1.3"><circle cx="12" cy="12" r="6"/><ellipse cx="12" cy="12" rx="2.6" ry="6"/><path d="M6 12h12M7 9h10M7 15h10"/></g></svg>
        <span>www.VestalukChirurgie</span>
      </li>
      <li class="contacts__item">
        <svg class="contacts__icon" viewBox="0 0 24 24"><circle cx="12" cy="12" r="12" fill="#fff"/><path d="M12 5a4.5 4.5 0 0 0-4.5 4.5C7.5 13 12 19 12 19s4.5-6 4.5-9.5A4.5 4.5 0 0 0 12 5z" fill="#45b9b6"/><circle cx="12" cy="9.5" r="1.7" fill="#fff"/></svg>
        <span>000 xxxxxx, xxxx,000,<br>xxxxxx</span>
      </li>
    </ul>
  </section>
</main>
</body>
</html>
```